Introducting Corbin Sheetmetal MADE WITH PRIDE

We require a PDF fact sheet that we can share via email that has a summary of infomation, services and products as found on our website www.corbinsheetmetal.example

The Call to Action - Heading should be "Made with Pride"

Needs to look professional, prefer sharp lines than bubble circles

Trying to attract new business

Target Market(s)

Potential new clients; Plumbers, Shop fitters, restaurants and Caters.

Industry/Entity Type

Manufacturing

Font styles to use
Other font styles liked:
• something masculine

Colors

Designer to choose colors to be used in the design.

Requirements
Must have
• Must be one page, low res so when emailing it's not too large.
• Must have phone number, email address and actual address
• Should include summary of copy from the website; www.corbinsheetmetal.example
• * A bit about us
• * Services
• * Fabrication Range and Finishes
• * General Fabrication
Nice to have
• Something that is not too busy, easy to read - so not too much writing. Must look professional (that's why we using ArtHive).
• Please let me know I you need images from the website and I'll sent to you.
Should not have
• It shouldn't be too busy, easy to read - so not too much writing. Simple and clear message.

```html
<!DOCTYPE html>
<html lang="en">
<head>
<meta charset="utf-8">
<title>Corbin Sheetmetal – Made With Pride</title>
<link href="https://fonts.googleapis.com/css2?family=Montserrat:ital,wght@0,400;0,600;0,700;0,800;1,400&family=Lato:ital,wght@0,400;0,700;1,400&display=swap" rel="stylesheet">
<style>
  :root{
    --slate:#47535e;
    --slate-dark:#3d4750;
    --ink:#3a3d40;
    --paper:#ffffff;
    --panel:#ecedef;
    --panel-right:#e2e4e7;
    --accent:#4d6a86;
    --stage:#dedfe0;
    --pride-fill:#e3e6e9;
  }
  *{box-sizing:border-box;margin:0;padding:0}
  html,body{width:1200px;height:1200px;overflow:hidden;background:var(--stage)}
  body{font-family:"Lato",sans-serif;color:var(--ink)}
  .sheet{position:absolute;left:172px;top:0;width:855px;height:1200px;background:var(--panel);overflow:hidden}
  .hero-art{position:absolute;left:0;top:0}
  .brand{position:absolute;left:62px;top:126px;display:flex;align-items:center;gap:8px;font-family:"Montserrat",sans-serif;font-weight:600;font-size:14px;letter-spacing:.5px;color:var(--slate)}
  .brand-mark{width:12px;height:12px;background:var(--slate)}
  .headline{position:absolute;left:50px;top:226px;font-family:"Montserrat",sans-serif;line-height:1}
  .headline-top{display:block;font-weight:700;font-size:47px;color:var(--slate);letter-spacing:-.5px}
  .headline-pride{display:block;margin-top:8px;font-weight:800;font-size:77px;color:var(--pride-fill);-webkit-text-stroke:2px #5d6872;letter-spacing:-1px}
  .right-panel{position:absolute;left:463px;top:500px;width:392px;height:600px;background:var(--panel-right)}
  .tag{position:absolute;height:24px;background:var(--slate);color:#fff;font-family:"Montserrat",sans-serif;font-size:17px;line-height:24px;padding-left:8px;clip-path:polygon(0 0,100% 0,calc(100% - 12px) 100%,0 100%);letter-spacing:.3px}
  .tag b{font-weight:800}
  .tag span{font-weight:400}
  .tag-about{left:52px;top:500px;width:195px}
  .tag-services{left:52px;top:750px;width:134px}
  .tag-general{left:475px;top:1006px;width:287px}
  .tag-facilities{left:463px;top:500px;width:392px;height:50px;line-height:21px;padding:5px 0 0 18px;clip-path:none;font-size:17px}
  .copy{position:absolute;font-size:12.3px;line-height:15.2px;text-align:justify}
  .copy p+p{margin-top:7px}
  .copy-about{left:52px;top:537px;width:350px}
  .copy-services{left:52px;top:783px;width:352px}
  .copy-more{left:52px;top:1105px;width:352px;text-align:left}
  .product-box{position:absolute;left:52px;top:923px;width:350px;height:165px;background:var(--slate);border-radius:10px;color:#fff;font-style:italic;font-size:12.7px}
  .product-box::after{content:"";position:absolute;left:163px;top:8px;bottom:8px;width:1px;background:#aeb6bd}
  .product-list{position:absolute;top:7px;list-style:none}
  .product-list li{display:flex;gap:8px;line-height:15px;margin-bottom:10px}
  .product-list li svg{flex:none;margin-top:2px}
  .product-list-a{left:9px;width:150px}
  .product-list-b{left:184px;width:162px}
  .pill{position:absolute;border:1.2px solid var(--accent);border-radius:10px;font-size:12.3px;line-height:15px;padding:2px 6px;color:var(--ink)}
  .pill em{font-style:normal;color:var(--accent)}
  .pill-equip{left:469px;top:558px;width:356px;height:35px;text-align:justify}
  .pill-materials{left:470px;top:707px;width:259px;height:24px}
  .pill-finishes{left:470px;top:843px;width:105px;height:24px}
  .checklist{position:absolute;list-style:none;font-size:12.3px}
  .checklist li{display:flex;align-items:center;gap:10px;height:25.5px}
  .list-equip{left:476px;top:599px}
  .list-materials{left:472px;top:734px}
  .list-finish-a{left:476px;top:872px}
  .list-finish-b{left:647px;top:872px}
  .finish-divider{position:absolute;left:617px;top:880px;width:1px;height:56px;background:#8c959d}
  .copy-design{left:475px;top:951px;width:350px;text-align:left;font-size:12.3px}
  .copy-design a{color:var(--accent);font-style:italic;text-decoration:none}
  .copy-general{left:475px;top:1040px;width:350px;text-align:left}
  .footer-bar{position:absolute;left:0;top:1153px;width:855px;height:47px;background:var(--slate)}
  .footer-contact{position:absolute;top:1163px;display:flex;align-items:center;gap:9px;color:#fff;font-size:12.3px}
  .contact-address{left:50px}
  .contact-email{left:369px}
  .phone-block{position:absolute;left:0;top:0}
  .phone{position:absolute;left:628px;top:1114px;display:flex;align-items:center;gap:8px;color:#fff;font-size:26px;font-family:"Lato",sans-serif}
  .web{position:absolute;left:612px;top:1160px;display:flex;align-items:center;gap:10px;color:#fff;font-size:12px}
</style>
</head>
<body>
<svg width="0" height="0" style="position:absolute">
  <symbol id="tick" viewBox="0 0 12 12">
    <circle cx="6" cy="6" r="5" fill="none" stroke="currentColor" stroke-width="1"/>
    <path d="M3.4 6.2l1.8 1.8 3.5-3.8" fill="none" stroke="currentColor" stroke-width="1.1"/>
  </symbol>
</svg>

<main class="sheet">
  <svg class="hero-art" width="855" height="500" viewBox="0 0 855 500">
    <defs>
      <linearGradient id="workshopTones" x1="0" y1="0" x2="1" y2="1">
        <stop offset="0" stop-color="#9a6a4e"/>
        <stop offset=".35" stop-color="#b8532f"/>
        <stop offset=".6" stop-color="#4f5048"/>
        <stop offset=".85" stop-color="#a8c23a"/>
        <stop offset="1" stop-color="#6b7a4a"/>
      </linearGradient>
    </defs>
    <polygon points="0,0 855,0 855,500 440,500 440,340 168,437 0,397" fill="var(--paper)"/>
    <polygon points="0,397 168,437 440,337 440,355 168,455 0,414" fill="var(--slate)"/>
    <polyline points="0,427 168,467 440,367" fill="none" stroke="var(--slate-dark)" stroke-width="2"/>
    <circle cx="618" cy="220" r="252" fill="var(--paper)" stroke="var(--slate)" stroke-width="1.5"/>
    <circle cx="618" cy="220" r="241" fill="none" stroke="#b9bfc5" stroke-width="3"/>
    <circle cx="618" cy="220" r="231" fill="none" stroke="var(--slate)" stroke-width="12"/>
    <circle cx="618" cy="220" r="222" fill="url(#workshopTones)" role="img" aria-label="Photo of a welder in a helmet and leather gloves welding metal with sparks flying"/>
  </svg>

  <div class="brand"><span class="brand-mark"></span>CORBIN SHEETMETAL</div>

  <h1 class="headline">
    <span class="headline-top">Made With</span>
    <span class="headline-pride">PRIDE</span>
  </h1>

  <div class="right-panel"></div>

  <h2 class="tag tag-about"><b>A BIT</b> <span>ABOUT US</span></h2>
  <div class="copy copy-about">
    <p>Fast, friendly, and fully functional, our professional Metal Fabrication Service is well renowned throughout South Australia. Our team is up for every job, managing projects with the skill and experience our clients have come to expect. We always stand behind our work, custom made with pride.Established in 1991, we are suppliers to the plumbing and mining trades, shop-fitters and builders, and the general public. We provide general sheetmetal and light steel fabrication services (cutting, folding, mig/tig welding) working with stainless steel, , copper, galvanised steel, aluminium and mild steel.</p>
    <p>As specialists in custom one-off and small-run manufacturing, take a look at some of our finished work and contact us with your enquiries.</p>
  </div>

  <h2 class="tag tag-services"><b>SERVICES</b></h2>
  <div class="copy copy-services">
    <p>We can produce and supply a range of sheet metal components for all industries. We supply to the plumbing, mining trades, shop-fitters, builders, and the general public. We provide general sheetmetal and light steel fabrication services (cutting, folding, mig/tig welding) working with stainless steel, aluminium, copper, galvanised steel and mild steel.</p>
    <p style="text-align:left">We can assist with a range of sheetmetal products using years of experience and a range of equipment.</p>
  </div>

  <div class="product-box">
    <ul class="product-list product-list-a">
      <li><svg width="11" height="11"><use href="#tick"/></svg>Commercial kitchen canopies</li>
      <li><svg width="11" height="11"><use href="#tick"/></svg>Shelvng</li>
      <li><svg width="11" height="11"><use href="#tick"/></svg>Tanks</li>
      <li><svg width="11" height="11"><use href="#tick"/></svg>Silt traps</li>
      <li><svg width="11" height="11"><use href="#tick"/></svg>Bench tops</li>
      <li><svg width="11" height="11"><use href="#tick"/></svg>Safety trays</li>
    </ul>
    <ul class="product-list product-list-b">
      <li><svg width="11" height="11"><use href="#tick"/></svg>Tundishes</li>
      <li><svg width="11" height="11"><use href="#tick"/></svg>Hand rails</li>
      <li><svg width="11" height="11"><use href="#tick"/></svg>Brackets</li>
      <li><svg width="11" height="11"><use href="#tick"/></svg>Mild Steel / Frame Work</li>
      <li><svg width="11" height="11"><use href="#tick"/></svg>Duct Work</li>
      <li><svg width="11" height="11"><use href="#tick"/></svg>Most Stainless Steel components</li>
    </ul>
  </div>

  <p class="copy copy-more">And much, much more. Contact us with your design and we will manufacture to order.</p>

  <h2 class="tag tag-facilities"><b>FACILITIES, MATERIALS &amp;</b><br><span>FINISHES</span></h2>

  <p class="pill pill-equip"><em>We Have an Extensive Range of Equipment</em> &amp; Sheet Metal Machinery That Includes:</p>
  <ul class="checklist list-equip">
    <li><svg width="11" height="11" style="color:#6d767e"><use href="#tick"/></svg>Hydraulic Pressbrake and Guillotine</li>
    <li><svg width="11" height="11" style="color:#6d767e"><use href="#tick"/></svg>Stenmark Copy Punch and notcher</li>
    <li><svg width="11" height="11" style="color:#6d767e"><use href="#tick"/></svg>Mechanical folders and plate roll</li>
    <li><svg width="11" height="11" style="color:#6d767e"><use href="#tick"/></svg>Extensive TIG and MIG welding equipment</li>
  </ul>

  <p class="pill pill-materials"><em>We Fabricate a Range</em> of Materials Including:</p>
  <ul class="checklist list-materials">
    <li><svg width="11" height="11" style="color:#6d767e"><use href="#tick"/></svg>Hydraulic Pressbrake and Guillotine</li>
    <li><svg width="11" height="11" style="color:#6d767e"><use href="#tick"/></svg>Stenmark Copy Punch and notcher</li>
    <li><svg width="11" height="11" style="color:#6d767e"><use href="#tick"/></svg>Mechanical folders and plate roll</li>
    <li><svg width="11" height="11" style="color:#6d767e"><use href="#tick"/></svg>Extensive TIG and MIG welding equipment</li>
  </ul>

  <p class="pill pill-finishes"><em>Finishes</em> Include:</p>
  <ul class="checklist list-finish-a">
    <li><svg width="11" height="11" style="color:#6d767e"><use href="#tick"/></svg>Polished</li>
    <li><svg width="11" height="11" style="color:#6d767e"><use href="#tick"/></svg>Powder-Coated</li>
    <li><svg width="11" height="11" style="color:#6d767e"><use href="#tick"/></svg>Painted</li>
  </ul>
  <div class="finish-divider"></div>
  <ul class="checklist list-finish-b">
    <li><svg width="11" height="11" style="color:#6d767e"><use href="#tick"/></svg>Mirrored</li>
    <li><svg width="11" height="11" style="color:#6d767e"><use href="#tick"/></svg>Textured</li>
  </ul>

  <p class="copy copy-design">We have experienced tradespeople with extensive experience and&nbsp; abilities to custom fabricate to your specific design.<br><a href="#">Contact us now</a></p>

  <h2 class="tag tag-general"><b>GENERAL</b> <span>FABRICATION</span></h2>
  <p class="copy copy-general">Wether you're performing shop fabrication, repairing equip-<br>ment on a farm or job site, or creating artwork in your garage,<br>Corbin Sheetmetal has the knowhow, creativity and process<br>knowledge to help you<br>get&nbsp;&nbsp; your&nbsp;&nbsp; job&nbsp;&nbsp; done<br>right.</p>

  <footer>
    <div class="footer-bar"></div>
    <svg class="phone-block" width="855" height="1200" viewBox="0 0 855 1200">
      <polygon points="618,1099 855,1099 855,1200 560,1200" fill="var(--slate)"/>
      <line x1="612" y1="1104" x2="572" y2="1200" stroke="#ffffff" stroke-width="4"/>
    </svg>
    <div class="footer-contact contact-address">
      <svg width="14" height="16" viewBox="0 0 14 16"><path d="M7 1a4.5 4.5 0 0 0-4.5 4.5C2.5 9 7 13 7 13s4.5-4 4.5-7.5A4.5 4.5 0 0 0 7 1z" fill="none" stroke="#fff" stroke-width="1.4"/><circle cx="7" cy="5.5" r="1.6" fill="#fff"/><line x1="1" y1="15" x2="13" y2="15" stroke="#fff" stroke-width="1.4"/></svg>
      14 Foundry Lane, Kestrel Park SA 5099, Australia
    </div>
    <div class="footer-contact contact-email">
      <svg width="15" height="15" viewBox="0 0 16 16"><circle cx="8" cy="8" r="7" fill="#fff"/><rect x="4" y="5.3" width="8" height="5.6" fill="none" stroke="var(--slate)" stroke-width="1.1"/><path d="M4 5.5l4 3 4-3" fill="none" stroke="var(--slate)" stroke-width="1.1"/></svg>
      info@corbinsheetmetal.example
    </div>
    <div class="phone">
      <svg width="18" height="18" viewBox="0 0 24 24"><path d="M6.6 10.8a15.1 15.1 0 0 0 6.6 6.6l2.2-2.2c.3-.3.7-.4 1-.2 1.1.4 2.3.6 3.6.6.6 0 1 .4 1 1V20c0 .6-.4 1-1 1A17 17 0 0 1 3 4c0-.6.4-1 1-1h3.5c.6 0 1 .4 1 1 0 1.3.2 2.5.6 3.6.1.3 0 .7-.2 1z" fill="#fff"/></svg>
      (08) 5550 1842
    </div>
    <div class="web">
      <svg width="18" height="18" viewBox="0 0 18 18"><circle cx="9" cy="9" r="8.5" fill="#fff"/><path d="M5 5.5c1.5 0 2 1 3 1.5s.5 2-.5 2.5-.5 2 .5 2.8M11 3.5c-.5 1 .5 2 1.5 2s1.5 1.5 1 2.5-1.5 1.5-1 3" fill="none" stroke="var(--slate)" stroke-width="1.4"/></svg>
      www.corbinsheetmetal.example
    </div>
  </footer>
</main>
</body>
</html>
```